VORN - Business cards

Business card to be created for Commercial sales staff

Target Market(s)

Commercial businesses

Industry/Entity Type

Commercial

Contact Information for Business Card

Look professional. For commercial clients

Colors
ffffff

Requirements
Must have
• - Vorn Logo
• - Commercial sales staff as postion
• - room for commerical sales manager role
• - person name and their mobile number
• - Website : vornelectrical.com.au
Nice to have
• White background.
• On back of business card just have the logo no other information
Should not have
• Should only have white background on front of card.

```html
<!DOCTYPE html>
<html lang="en">
<head>
<meta charset="utf-8">
<title>VORN – Business Cards</title>
<link rel="stylesheet" href="https://fonts.googleapis.com/css2?family=Open+Sans:wght@400;700;800&display=swap">
<style>
  :root {
    --backdrop: #2b2b2b;
    --card: #ffffff;
    --ink: #231f20;
    --accent: #d71920;
    --muted: #3a3a3a;
  }
  * { box-sizing: border-box; margin: 0; padding: 0; }
  html, body {
    width: 1200px;
    height: 660px;
    overflow: hidden;
    background: var(--backdrop);
    font-family: "Open Sans", Arial, sans-serif;
  }
  .sheet {
    width: 1200px;
    height: 660px;
    display: flex;
    align-items: center;
    justify-content: center;
    gap: 60px;
  }
  .card {
    position: relative;
    width: 520px;
    height: 300px;
    background: var(--card);
    box-shadow: 0 10px 30px rgba(0,0,0,.45);
  }
  .brand {
    display: flex;
    align-items: center;
    gap: 10px;
    color: var(--ink);
    font-weight: 800;
    letter-spacing: 1px;
    line-height: 1;
  }
  .brand-dot {
    border-radius: 50%;
    background: var(--accent);
  }
  .card-front .brand {
    position: absolute;
    top: 34px;
    right: 40px;
    font-size: 34px;
  }
  .card-front .brand-dot { width: 22px; height: 22px; }
  .contact {
    position: absolute;
    left: 40px;
    bottom: 40px;
  }
  .person-name {
    font-size: 22px;
    font-weight: 400;
    color: var(--ink);
    line-height: 1.1;
  }
  .person-role {
    font-size: 13px;
    color: var(--accent);
    margin-bottom: 10px;
  }
  .contact-list { list-style: none; }
  .contact-list li {
    display: flex;
    align-items: center;
    gap: 8px;
    font-size: 12.5px;
    color: var(--muted);
    line-height: 1.55;
  }
  .contact-list svg { width: 12px; height: 12px; flex: none; }
  .card-back {
    display: flex;
    align-items: center;
    justify-content: center;
  }
  .card-back .brand { font-size: 64px; gap: 16px; }
  .card-back .brand-dot { width: 40px; height: 40px; }
</style>
</head>
<body>
  <main class="sheet">
    <section class="card card-front" aria-label="Card front">
      <div class="brand"><span class="brand-dot"></span><span>VORN</span></div>
      <div class="contact">
        <p class="person-name">Name Surname</p>
        <p class="person-role">Designation</p>
        <ul class="contact-list">
          <li>
            <svg viewBox="0 0 12 12" aria-hidden="true"><rect x="3" y="0.8" width="6" height="10.4" rx="1.2" fill="none" stroke="var(--accent)" stroke-width="1.3"/><circle cx="6" cy="9.2" r="0.7" fill="var(--accent)"/></svg>
            (000) 000-0000
          </li>
          <li>
            <svg viewBox="0 0 12 12" aria-hidden="true"><rect x="0.5" y="2" width="11" height="8" fill="var(--accent)"/><path d="M0.8 2.4 L6 6.6 L11.2 2.4" fill="none" stroke="#fff" stroke-width="1.1"/></svg>
            username@vornelectrical.com.au
          </li>
          <li>
            <svg viewBox="0 0 12 12" aria-hidden="true"><circle cx="6" cy="6" r="5.2" fill="none" stroke="var(--accent)" stroke-width="1.2"/><ellipse cx="6" cy="6" rx="2.2" ry="5.2" fill="none" stroke="var(--accent)" stroke-width="1"/><path d="M0.8 6 H11.2 M1.8 3.4 H10.2 M1.8 8.6 H10.2" stroke="var(--accent)" stroke-width="0.9"/></svg>
            vornelectrical.com.au
          </li>
        </ul>
      </div>
    </section>
    <section class="card card-back" aria-label="Card back">
      <div class="brand"><span class="brand-dot"></span><span>VORN</span></div>
    </section>
  </main>
</body>
</html>
```